Brightwell cleaning and maintenance company

An expansive website whereby we can advertise our commercial cleaning and maintenance services across a service portfolio of commercial cleaning and property maintenance. Whereby potential skilled resources can deposit there resume so we can collaborate and match candidates to a broad range of cleaning and maintenance jobs/projects.
Updates

Looking for more extensive ideas so the front page can change pictures on it with the focus for Brightwell Commercial Cleaning and Maintenance. Also need to bring in all the portfolios we offer including 1. Equipment Cleaning and Sanitisation Services 2. High pressure gurney and play ground equipment cleaning 3. General Cleaning and Property Facilities Management 4. Project and Recruiting Services, to allow for potential professional cleaners, handy man, mechanics, warehousing resources , electricians to deposit there resume. Most of the designers have stuck with the old portfolio categories , however the portfolio of services we offer has been updated so that needs to be reflected in the website. Also not necessary to use all my original photos I would like the opening page of the website to perhaps be able to change and have different pictures is that possible thank you

```html
<!DOCTYPE html>
<html lang="en">
<head>
<meta charset="utf-8">
<title>Brightwell – Website Concept</title>
<link href="https://fonts.googleapis.com/css2?family=Merriweather:ital,wght@0,300;0,400;0,700;0,900;1,400&display=swap" rel="stylesheet">
<style>
:root{
  --navy:#1a3c7a;
  --navy-dark:#14306a;
  --orange:#f15a22;
  --white:#ffffff;
  --ink:#2c2c2c;
  --muted:#7a7a7a;
  --soft:#f3f4f6;
  --board:#eceef2;
}
*{box-sizing:border-box;margin:0;padding:0}
html,body{width:1200px;height:3654px;overflow:hidden}
body{font-family:"Merriweather",Georgia,serif;background:var(--board);color:var(--ink);position:relative}

.board-backdrop{position:absolute;left:0;top:0;width:1200px;height:700px;
  background:linear-gradient(180deg,#232427 0,#3d3f43 200px,#6a6c71 360px,#b9bbc0 520px,var(--board) 700px)}
.board-brand{position:absolute;left:150px;top:112px;display:flex;align-items:center;gap:34px}
.board-brand .dot{width:150px;height:150px;border-radius:50%;background:var(--white)}
.board-brand .name{font-size:118px;font-weight:400;color:var(--white);letter-spacing:1px;line-height:1}

.mock{position:absolute;width:448px;background:var(--white);box-shadow:0 6px 22px rgba(20,30,60,.18);overflow:hidden}
.mock-home{left:126px;top:355px;height:3193px}
.mock-hero{left:625px;height:310px}

.topbar{height:17px;border-top:2px solid var(--orange);display:flex;justify-content:flex-end;align-items:center;gap:10px;padding-right:22px;font-size:4.6px;color:var(--navy);white-space:nowrap}
.topbar span{display:flex;align-items:center;gap:3px}
.topbar i{display:inline-block;width:7px;height:7px;background:var(--orange);border-radius:1px}
.topbar b{font-size:6.4px;font-weight:700}
.nav{height:39px;display:flex;align-items:center;justify-content:space-between;padding:0 28px 0 28px}
.logo{display:flex;align-items:center;gap:4px;font-size:13px;color:var(--navy);font-weight:400}
.logo i{width:11px;height:11px;border-radius:50%;background:var(--navy)}
.menu{display:flex;gap:10px;font-size:4.6px;color:#777;letter-spacing:.2px;white-space:nowrap}
.menu .on{color:var(--orange)}

.hero{position:relative;height:227px;overflow:hidden}
.hero-photo{position:absolute;inset:0}
.ph-office{background:linear-gradient(120deg,#5e6c7e 0,#8a96a6 35%,#3e5a86 60%,#6e7d90 100%)}
.ph-kitchen{background:linear-gradient(115deg,#2d3036 0,#6d7179 40%,#3a3d44 70%,#8a5a3c 100%)}
.ph-pressure{background:linear-gradient(125deg,#5c5e58 0,#8b8c84 40%,#c9cdd1 55%,#6e6f68 100%)}
.ph-sundae{background:linear-gradient(115deg,#4b4a48 0,#a39d92 35%,#2f2e2d 65%,#1f1f20 100%)}
.hero-title{position:absolute;left:205px;top:90px;width:200px;font-size:19px;line-height:1.15;font-weight:400;color:var(--white);text-shadow:0 1px 3px rgba(0,0,0,.35)}
.pips{position:absolute;right:22px;top:100px;width:10px;height:66px;background:var(--white);border-radius:5px;display:flex;flex-direction:column;align-items:center;justify-content:space-evenly;padding:4px 0}
.pips i{width:4px;height:4px;border-radius:50%;background:var(--navy)}
.pips i:first-child{background:var(--orange)}
.hero-wave{position:absolute;left:0;bottom:0;width:448px;height:46px}

.sec{position:relative;overflow:hidden}
.h-sec{font-size:14px;font-weight:700;text-align:center;color:var(--navy)}
.h-sec em{font-style:normal;color:var(--orange)}
.on-navy .h-sec{color:var(--white)}
.tiny{font-size:4.5px;line-height:1.55;color:var(--muted)}
.btn{display:inline-flex;align-items:center;gap:4px;height:11px;padding:0 0 0 9px;background:var(--orange);color:var(--white);font-size:4.8px;border-radius:6px;white-space:nowrap}
.btn i{width:11px;height:11px;border-radius:50%;background:var(--navy)}
.dots{display:flex;justify-content:center;gap:5px}
.dots i{width:4px;height:4px;border-radius:50%;background:var(--orange)}
.dots i.on{background:var(--navy)}
.on-navy .dots i.on{background:var(--white)}
.navy{background:var(--navy)}

.welcome{height:166px;text-align:center;padding:20px 62px 0}
.welcome .h-sec{font-size:15px;margin-bottom:12px}
.welcome .tiny{margin-bottom:7px}

.services{height:184px;background:var(--soft);padding-top:22px}
.svc-row{display:flex;gap:9px;justify-content:center;margin-top:17px}
.svc{width:90px;height:86px;background:var(--white);box-shadow:0 1px 3px rgba(0,0,0,.12);position:relative}
.svc .img{height:58px}
.svc .cap{position:absolute;left:6px;right:6px;bottom:4px;height:28px;background:var(--white);text-align:right;padding:3px 4px;font-size:3.8px;color:var(--ink);line-height:1.3}
.svc .cap b{display:block;font-size:7px;font-weight:400;color:var(--navy);margin-top:1px}
.svc.first .cap{background:var(--orange);color:var(--white)}
.svc.first .cap b{color:var(--white)}
.services .dots{margin-top:14px}

.working{height:250px;background:linear-gradient(180deg,var(--white),#f6f7f9)}
.working .art{position:absolute;left:22px;top:0;width:200px;height:228px;border-radius:48% 52% 46% 54%/50% 44% 56% 50%}
.working .copy{position:absolute;left:228px;top:38px;width:186px}
.working .kick{font-size:8px;color:var(--navy)}
.working .big{font-size:15px;font-weight:700;color:var(--orange);margin:1px 0 7px}
.working .lead{font-size:5.6px;color:var(--ink);line-height:1.4;margin-bottom:7px}
.working .tiny{margin-bottom:7px}

.pricing{height:244px;padding-top:24px}
.price-row{display:flex;gap:6px;justify-content:center;margin-top:18px}
.price{width:92px;height:118px;background:var(--white);padding:10px 8px;position:relative}
.price h4{font-size:7.4px;line-height:1.2;color:var(--navy);font-weight:400;height:40px;padding-right:14px}
.price .amt{font-size:15px;color:var(--orange)}
.price .gst{font-size:4.8px;color:var(--muted);margin-top:2px}
.price .note{font-size:3.8px;color:var(--muted);margin-top:8px;line-height:1.4}
.price .call{position:absolute;right:6px;top:13px;width:16px;height:16px;border-radius:50%;background:var(--orange);display:flex;align-items:center;justify-content:center}
.pricing .dots{margin-top:24px}

.gallery{height:432px;padding-top:34px}
.gal{position:absolute}

.reviews{height:230px;padding-top:32px;text-align:center}
.reviews .h-sec{color:var(--orange);font-size:12px}
.quote-mark{font-size:32px;color:var(--orange);line-height:.8;margin-top:10px;height:22px}
.reviews blockquote{font-size:9.6px;font-style:italic;color:var(--white);line-height:1.35;width:320px;margin:6px auto 0}
.arrow{position:absolute;top:108px;width:9px;height:9px;border-left:1.5px solid rgba(255,255,255,.45);border-bottom:1.5px solid rgba(255,255,255,.45)}
.stars{display:flex;gap:3px;justify-content:center;margin-top:18px}
.stars i{width:9px;height:9px;border-radius:50%;background:var(--orange)}
.reviewer{font-size:5.6px;color:var(--white);margin-top:7px}
.reviewer small{display:block;font-size:4.2px;opacity:.7;font-style:italic}

.values{height:203px;display:flex;gap:13px;justify-content:center;padding-top:22px}
.val{width:122px}
.val .box{height:80px;background:var(--orange);display:flex;align-items:center;justify-content:center}
.val h5{font-size:8px;font-weight:700;color:var(--navy);margin:6px 0 4px 3px}
.val h5 em{font-style:normal;color:var(--orange)}
.val .tiny{padding-left:3px}

.careers{height:266px;background:linear-gradient(90deg,var(--soft),#fafafa)}
.careers .copy{position:absolute;left:27px;top:32px;width:140px}
.careers h3{font-size:15px;font-weight:700;color:var(--navy);margin-bottom:10px}
.field{height:15px;background:var(--white);border:1px solid #ddd;font-size:4.4px;color:var(--muted);display:flex;align-items:center;justify-content:space-between;padding:0 6px;margin-top:8px;width:140px}
.careers .btn{margin-top:10px}
.careers .photo{position:absolute;left:186px;top:0;width:262px;height:266px}

.portfolio{height:284px;padding-top:24px}
.partners{margin:20px 27px 0;height:74px;background:var(--white);display:flex;align-items:center;justify-content:space-evenly}
.partners i{display:block;width:42px;height:16px;background:#d7dae0;border-radius:2px}
.partners i:nth-child(2n){width:22px;height:22px;border-radius:50%}
.story{margin:18px 27px 0;height:100px;background:var(--white);padding:14px 14px;position:relative}
.story h6{font-size:6px;color:var(--orange);font-weight:700;margin-bottom:6px}
.story .tiny{width:250px;color:var(--navy)}
.story .sign{font-size:6px;font-style:italic;color:#9aa;margin-top:6px}
.story .mark{position:absolute;right:26px;top:26px;width:46px;height:38px;background:#d7dae0;border-radius:3px}

.blog{height:244px;padding-top:36px}
.blog-row{display:flex;gap:10px;justify-content:center;margin-top:18px}
.post{width:124px;height:155px;background:var(--white);box-shadow:0 1px 4px rgba(0,0,0,.14)}
.post .img{height:91px;position:relative}
.post .img .btn{position:absolute;left:22px;top:44px;height:10px;font-size:4.4px;padding:0 10px}
.post h6{font-size:6px;font-weight:400;color:var(--ink);margin:9px 10px 4px;line-height:1.2;border-left:2px solid var(--orange);padding-left:5px}
.post .tiny{font-size:3.8px;margin:0 10px}
.post .meta{display:flex;justify-content:space-between;font-size:3.8px;color:var(--navy);margin:14px 10px 0;border-top:1px solid #eee;padding-top:4px}

.safety{height:224px;padding:34px 70px 0;text-align:center}
.safety .h-sec{color:var(--orange);margin-bottom:18px}
.safety .h-sec em{color:var(--white)}
.safety .tiny{color:#dfe6f3;margin-bottom:8px}

.foot{height:102px;text-align:center;padding-top:24px}
.foot .logo{justify-content:center}
.foot .menu{justify-content:center;margin-top:14px}
.foot .contact{display:flex;justify-content:center;gap:12px;font-size:4.4px;color:var(--navy);margin-top:10px;white-space:nowrap}
.social{height:81px;background:var(--orange);padding-top:20px;text-align:center;color:var(--white)}
.social-row{display:flex;justify-content:center;gap:16px}
.social-row span{display:flex;flex-direction:column;align-items:center;gap:5px;font-size:5px;letter-spacing:.2px}
.social-row i{width:8px;height:8px;border-radius:50%;background:var(--white)}
.social .copy{font-size:4.4px;margin-top:12px}
</style>
</head>
<body>

<div class="board-backdrop" role="img" aria-label="Dimmed photo of a stainless steel commercial kitchen with extraction hoods"></div>
<div class="board-brand"><span class="dot"></span><span class="name">Brightwell</span></div>

<div class="mock mock-home">
  <div class="topbar">
    <span><i></i>EMAIL : service@brightwell.com.au</span>
    <span><i></i><b>HEAD OFFICE: 1800 670 225</b></span>
  </div>
  <div class="nav">
    <div class="logo"><i></i>Brightwell</div>
    <div class="menu"><span class="on">HOME</span><span>ABOUT</span><span>SERVICES</span><span>PORTFOLIO</span><span>REVIEWS</span><span>CONTACT US</span></div>
  </div>
  <div class="hero">
    <div class="hero-photo ph-office" role="img" aria-label="Cleaners in blue uniforms mopping and wiping an office"></div>
    <h2 class="hero-title">Office cleaning</h2>
    <div class="pips"><i></i><i></i><i></i><i></i></div>
    <svg class="hero-wave" viewBox="0 0 448 46" preserveAspectRatio="none"><path d="M0,14 C110,44 260,44 448,4 L448,46 L0,46Z" fill="#fff"/><path d="M0,14 C110,44 260,44 448,4" fill="none" stroke="#1a3c7a" stroke-width="4"/></svg>
  </div>

  <section class="sec welcome">
    <h2 class="h-sec">Welcome To <em>Brightwell</em></h2>
    <p class="tiny">We have been in the Commercial Cleaning and Maintenance business for 12 years.<br>We have built a strong and steady reputation. Our people are professional, reliable and customer service focused.</p>
    <p class="tiny">Our business strategy is to align strong and professionally skilled resources to each of our customers with a focus on a quality driven service, to create a dynamic and positive work environment. Our purpose is to provide high quality hygiene and sanitisation services to each of our dedicated portfolios across equipment cleaning services, gurney and playground cleaning, general commercial cleaning and property facilities maintenance services for our customers and community.</p>
    <span class="btn">Read More <i></i></span>
  </section>

  <section class="sec services">
    <h2 class="h-sec"><em>Our</em> Services</h2>
    <div class="svc-row">
      <div class="svc first"><div class="img" style="background:linear-gradient(135deg,#7d8794,#c4cad2)" role="img" aria-label="Steel equipment being sanitised"></div><div class="cap">Equipment Cleaning &amp; Sanitisation<b>Services</b></div></div>
      <div class="svc"><div class="img" style="background:linear-gradient(135deg,#b8c2cf,#6e86a8)" role="img" aria-label="Cleaner in a bright office"></div><div class="cap">General Cleaning &amp; Property Facilities<b>Management</b></div></div>
      <div class="svc"><div class="img" style="background:linear-gradient(135deg,#5a6a78,#9aa6b0)" role="img" aria-label="Pressure washing a stone wall"></div><div class="cap">High pressure gurney &amp; play ground equipment<b>Cleaning</b></div></div>
      <div class="svc"><div class="img" style="background:linear-gradient(135deg,#4a5160,#a0a4aa)" role="img" aria-label="Team meeting around a table"></div><div class="cap">Projects and Recruiting Services<b>Work with us</b></div></div>
    </div>
    <div class="dots"><i></i><i class="on"></i><i></i></div>
  </section>

  <section class="sec working">
    <div class="art" style="background:linear-gradient(140deg,#cfd6e0,#8ea3c4 45%,#e3b27a 70%,#dfe4ea)" role="img" aria-label="Collage of cleaners with spray bottles and buckets"></div>
    <div class="copy">
      <div class="kick">Working with</div>
      <div class="big">Brightwell</div>
      <p class="lead">We are Brightwell, a leading, Australian owned, cleaning services company.</p>
      <p class="tiny">When you work with Brightwell it is easy to do business with us. We have been in the equipment services industry for close to 15 years.</p>
      <p class="tiny">Our people are professional, reliable and service oriented. In every interaction you have, on site, receiving help from our service support staff, or rolling out new cleaning sites, you will see and feel the benefits of using Brightwell.</p>
      <span class="btn">Read More <i></i></span>
    </div>
  </section>

  <section class="sec pricing navy on-navy">
    <h2 class="h-sec"><em>Current</em> pricing</h2>
    <div class="price-row">
      <div class="price"><h4>Internal detail equipment cleaning</h4><div class="amt">$100.00</div><div class="gst">+ GST per hour</div></div>
      <div class="price"><h4>Gurney high pressure work</h4><div class="amt">$100.00</div><div class="gst">+ GST per hour</div></div>
      <div class="price"><span class="call"><svg width="8" height="8" viewBox="0 0 24 24"><path d="M6.6 10.8a15 15 0 006.6 6.6l2.2-2.2c.3-.3.7-.4 1-.2 1.1.4 2.3.6 3.6.6.6 0 1 .4 1 1V20c0 .6-.4 1-1 1A17 17 0 013 4c0-.6.4-1 1-1h3.5c.6 0 1 .4 1 1 0 1.3.2 2.5.6 3.6.1.3 0 .7-.2 1z" fill="#fff"/></svg></span><h4>Builders cleaning services</h4><div class="amt">$100.00</div><div class="gst">+ GST</div><p class="note">* Pls say subfloat personnel for the waste disposal</p></div>
      <div class="price"><h4>General Commercial Cleaning</h4><div class="amt">$ 60.00</div><div class="gst">+ GST per hour</div></div>
    </div>
    <div class="dots"><i></i><i class="on"></i><i></i></div>
  </section>

  <section class="sec gallery">
    <h2 class="h-sec"><em>Our</em> Photo Gallery</h2>
    <div class="gal" style="left:27px;top:74px;width:128px;height:157px;background:linear-gradient(135deg,#9aa3ad,#e1e5ea 55%,#7f8a96)" role="img" aria-label="Clean slushie machines"></div>
    <div class="gal" style="left:27px;top:238px;width:128px;height:114px;background:linear-gradient(135deg,#8a9a6e,#e9e2d6 55%,#6b7c8c)" role="img" aria-label="Cleaner wiping a window"></div>
    <div class="gal" style="left:160px;top:74px;width:128px;height:110px;background:linear-gradient(135deg,#e07a4e,#f2b08c 55%,#c55a30)" role="img" aria-label="Inside of a copper machine drum"></div>
    <div class="gal" style="left:160px;top:191px;width:128px;height:114px;background:linear-gradient(135deg,#5b6f8a,#c7b38c 55%,#3f4f66)" role="img" aria-label="Staff walking through a warehouse"></div>
    <div class="gal" style="left:160px;top:312px;width:128px;height:85px;background:linear-gradient(135deg,#c74d4d,#e9b84a 45%,#4a78b8)" role="img" aria-label="Children's indoor playground"></div>
    <div class="gal" style="left:294px;top:74px;width:127px;height:171px;background:linear-gradient(135deg,#4f6d3f,#b8bdb4 55%,#7c8c70)" role="img" aria-label="Pressure washing paving beside a lawn"></div>
    <div class="gal" style="left:294px;top:252px;width:127px;height:145px;background:linear-gradient(135deg,#6f88c4,#d85a8a 55%,#d9d2e8)" role="img" aria-label="Pink playground slide"></div>
  </section>

  <section class="sec reviews navy">
    <h2 class="h-sec">Reviews</h2>
    <div class="quote-mark">&ldquo;</div>
    <span class="arrow" style="left:40px;transform:rotate(45deg)"></span>
    <span class="arrow" style="right:40px;transform:rotate(-135deg)"></span>
    <blockquote>Sed ut perspiciatis unde omnis iste natus error sit voluptatem accusantium doloremque laudantium, totam rem aperiam, eaque ipsa quae ab illo.</blockquote>
    <div class="stars"><i></i><i></i><i></i><i></i><i></i></div>
    <div class="reviewer">Dana R.<small>Cupi ipsum dolor</small></div>
  </section>

  <section class="sec values">
    <div class="val">
      <div class="box"><svg width="34" height="34" viewBox="0 0 34 34" fill="none" stroke="#fff" stroke-width="2"><circle cx="13" cy="10" r="5"/><circle cx="22" cy="12" r="4"/><path d="M17 16v8M9 24h16l-2 7H11z"/></svg></div>
      <h5><em>Our</em> Purpose</h5>
      <p class="tiny">To provide high quality hygiene and sanitisation services to commercial working environments and maximise the life of equipment and to create the most effective yield and healthy sanitised environments for our customers and community.</p>
    </div>
    <div class="val">
      <div class="box"><svg width="40" height="40" viewBox="0 0 40 40"><path d="M20 2 L23 17 L38 20 L23 23 L20 38 L17 23 L2 20 L17 17Z" fill="#fff"/></svg></div>
      <h5><em>Our</em> Vision</h5>
      <p class="tiny">Sustainable commercial environments and maintenance service equipment cleaning and sanitisation service provider. Recognised as being the most effective brand, growing employees and giving back to the community for generations to come.</p>
    </div>
    <div class="val">
      <div class="box"><svg width="36" height="36" viewBox="0 0 36 36" fill="none" stroke="#fff" stroke-width="2"><circle cx="18" cy="18" r="15"/><path d="M11 25 L16 16 L25 11 L20 20Z"/></svg></div>
      <h5><em>Our</em> Strategy</h5>
      <p class="tiny">To differentiate ourselves through a prevailing focus on customer service, in everything we do and every interaction we have is to be a positive and professional experience. We trust our people as skilled cleaning professionals who are the foundation of our company sustainability.</p>
    </div>
  </section>

  <section class="sec careers">
    <div class="copy">
      <h3>Careers</h3>
      <p class="tiny">We offer a professional and positive working environment. We are looking for professionals who are focused on high quality results, are highly motivated and ability to build great positive working relationships with our clients. We have a collaborative approach to working with professional business partners in the Cleaning and Maintenance Industry.</p>
      <div class="field" style="margin-top:14px">Professional careers photo <span>&#8599;</span></div>
      <div class="field">Attach you Resume <span>&#8599;</span></div>
      <span class="btn">Submit <i></i></span>
    </div>
    <div class="photo" style="background:linear-gradient(120deg,#d9dde3,#3b5ea8 40%,#a45a3e 75%,#d7c2ae)" role="img" aria-label="Team of cleaners in blue overalls with vacuum and wet floor sign"></div>
  </section>

  <section class="sec portfolio navy on-navy">
    <h2 class="h-sec">Portfolio</h2>
    <div class="partners"><i></i><i></i><i></i><i></i><i></i><i></i></div>
    <div class="story">
      <h6>OUR SUCCESS STORIES</h6>
      <p class="tiny">Lorem ipsum dolor sit amet, consectetur adipiscing elit, sed do eiusmod tempor incididunt ut labore et dolore magna aliqua. Ut enim ad minim veniam, quis nostrud exercitation ullamco laboris nisi ut aliquip ex ea commodo consequat. Duis aute irure dolor in reprehenderit in voluptate velit esse</p>
      <p class="sign">Harvest Grill Director</p>
      <span class="mark"></span>
    </div>
  </section>

  <section class="sec blog">
    <h2 class="h-sec"><em>Latest</em> Blog</h2>
    <div class="blog-row">
      <div class="post"><div class="img" style="background:linear-gradient(135deg,#3e5e94,#9aa9bd)" role="img" aria-label="Cleaner working in an office"><span class="btn">Read more</span></div><h6>I must explain to you how all this mistaken idea</h6><p class="tiny">Nor again is there anyone who loves or pursues or desires to obtain pain of</p><div class="meta"><span>Brightwell</span><span>&#9825; 12</span></div></div>
      <div class="post"><div class="img" style="background:linear-gradient(135deg,#e6e9ee,#7f99c2)" role="img" aria-label="Cleaner mopping a bright room"></div><h6>I must explain to you how all this mistaken idea</h6><p class="tiny">Nor again is there anyone who loves or pursues or desires to obtain pain of</p><div class="meta"><span>Brightwell</span><span>&#9825; 12</span></div></div>
      <div class="post"><div class="img" style="background:linear-gradient(135deg,#6a5a40,#9ba07c)" role="img" aria-label="Pressure washing a garden path"></div><h6>I must explain to you how all this mistaken idea</h6><p class="tiny">Nor again is there anyone who loves or pursues or desires to obtain pain of</p><div class="meta"><span>Brightwell</span><span>&#9825; 12</span></div></div>
    </div>
  </section>

  <section class="sec safety navy">
    <h2 class="h-sec">Safety <em>and</em> Compliance</h2>
    <p class="tiny">Brightwell values safety and environment. We have an overriding commitment to health, safety and environmental responsibility.</p>
    <p class="tiny">Each member of our company community undergoes a yearly on-line safety refresher course, and performs a routine reflection safety check and risk assessment at each clients site on attending work each day. We have safety work method statements in place and work on ensuring our people work safely on site through practical application of safety steps, safety shoes and appropriate personal protection equipment (PPE) work gear.</p>
    <span class="btn">Read More <i></i></span>
  </section>

  <footer class="foot">
    <div class="logo"><i></i>Brightwell</div>
    <div class="menu"><span class="on">HOME</span><span>ABOUT</span><span>SERVICES</span><span>PORTFOLIO</span><span>REVIEWS</span><span>CONTACT US</span></div>
    <div class="contact"><span>&#9990; Landline: 1800 670 225</span><span>| &#9743; Mobile: 0400 881 602</span><span>| &#9993; service@brightwell.com.au</span></div>
  </footer>
  <div class="social">
    <div class="social-row"><span><i></i>CIRCLEPAGE</span><span><i></i>SNAPFRAME</span><span><i></i>CHIRPLINE</span><span><i></i>WORKMESH</span></div>
    <div class="copy">&copy; 2021 | www.brightwell.com.au</div>
  </div>
</div>

<div class="mock mock-hero" style="top:355px">
  <div class="topbar"><span><i></i>EMAIL : service@brightwell.com.au</span><span><i></i><b>HEAD OFFICE: 1800 670 225</b></span></div>
  <div class="nav"><div class="logo"><i></i>Brightwell</div><div class="menu"><span class="on">HOME</span><span>ABOUT</span><span>SERVICES</span><span>PORTFOLIO</span><span>REVIEWS</span><span>CONTACT US</span></div></div>
  <div class="hero">
    <div class="hero-photo ph-kitchen" role="img" aria-label="Commercial kitchen with steel benches and hoods"></div>
    <h2 class="hero-title" style="top:76px;width:140px">Brightwell Service</h2>
    <div class="pips"><i></i><i></i><i></i><i></i></div>
    <svg class="hero-wave" viewBox="0 0 448 46" preserveAspectRatio="none"><path d="M0,14 C110,44 260,44 448,4 L448,46 L0,46Z" fill="#fff"/><path d="M0,14 C110,44 260,44 448,4" fill="none" stroke="#1a3c7a" stroke-width="4"/></svg>
  </div>
</div>

<div class="mock mock-hero" style="top:706px">
  <div class="topbar"><span><i></i>EMAIL : service@brightwell.com.au</span><span><i></i><b>HEAD OFFICE: 1800 670 225</b></span></div>
  <div class="nav"><div class="logo"><i></i>Brightwell</div><div class="menu"><span class="on">HOME</span><span>ABOUT</span><span>SERVICES</span><span>PORTFOLIO</span><span>REVIEWS</span><span>CONTACT US</span></div></div>
  <div class="hero">
    <div class="hero-photo ph-pressure" role="img" aria-label="High pressure water jet cleaning pavement"></div>
    <h2 class="hero-title" style="left:218px;top:80px;width:165px">High Preasure Water Cleaning</h2>
    <div class="pips"><i></i><i></i><i></i><i></i></div>
    <svg class="hero-wave" viewBox="0 0 448 46" preserveAspectRatio="none"><path d="M0,14 C110,44 260,44 448,4 L448,46 L0,46Z" fill="#fff"/><path d="M0,14 C110,44 260,44 448,4" fill="none" stroke="#1a3c7a" stroke-width="4"/></svg>
  </div>
</div>

<div class="mock mock-hero" style="top:1058px">
  <div class="topbar"><span><i></i>EMAIL : service@brightwell.com.au</span><span><i></i><b>HEAD OFFICE: 1800 670 225</b></span></div>
  <div class="nav"><div class="logo"><i></i>Brightwell</div><div class="menu"><span class="on">HOME</span><span>ABOUT</span><span>SERVICES</span><span>PORTFOLIO</span><span>REVIEWS</span><span>CONTACT US</span></div></div>
  <div class="hero">
    <div class="hero-photo ph-sundae" role="img" aria-label="Dessert bar with a soft serve machine"></div>
    <h2 class="hero-title" style="top:70px;width:210px">Sundae equipment cleaning</h2>
    <div class="pips"><i></i><i></i><i></i><i></i></div>
    <svg class="hero-wave" viewBox="0 0 448 46" preserveAspectRatio="none"><path d="M0,14 C110,44 260,44 448,4 L448,46 L0,46Z" fill="#fff"/><path d="M0,14 C110,44 260,44 448,4" fill="none" stroke="#1a3c7a" stroke-width="4"/></svg>
  </div>
</div>

<div class="mock mock-hero" style="top:1394px">
  <div class="topbar"><span><i></i>EMAIL : service@brightwell.com.au</span><span><i></i><b>HEAD OFFICE: 1800 670 225</b></span></div>
  <div class="nav"><div class="logo"><i></i>Brightwell</div><div class="menu"><span class="on">HOME</span><span>ABOUT</span><span>SERVICES</span><span>PORTFOLIO</span><span>REVIEWS</span><span>CONTACT US</span></div></div>
  <div class="hero">
    <div class="hero-photo ph-office" role="img" aria-label="Cleaners in blue uniforms mopping and wiping an office"></div>
    <h2 class="hero-title" style="top:88px">Office cleaning</h2>
    <div class="pips"><i></i><i></i><i></i><i></i></div>
    <svg class="hero-wave" viewBox="0 0 448 46" preserveAspectRatio="none"><path d="M0,14 C110,44 260,44 448,4 L448,46 L0,46Z" fill="#fff"/><path d="M0,14 C110,44 260,44 448,4" fill="none" stroke="#1a3c7a" stroke-width="4"/></svg>
  </div>
</div>

</body>
</html>
```